Web design for a relaunch of a technology and knowledge transfer company

Design for the relaunch of an existing website The company specializes in technology and knowledge transfer between companies (and universities). The innovation company (company name) combines many years of experience in technology transfer, innovation management, project management and grant applications. Link: http://www.fortschrittswerkhaus.example The colors of the logo are not very advantageous and can be adjusted a bit. There are currently no picture worlds, these are to be selected by the designer. Abstract motifs are certainly an advantage here (10 motifs). Animated programming could be done (network etc. http://valmeta.brixlane.example/). In this case a suggestion is made, which we convert programming technically. The structure and contents of the existing pages will be adopted and supplemented. The programming will be done with TYPO3 in responsive form (bootstrap). Required are start page, content page and contact page. -------------------------------------------------- ------------------------------ Web design for a relaunch of a company in technology and knowledge transfer Design for the relaunch of an existing website. The company specializes in technology and knowledge transfer between companies (and universities). The innovation company combines many years of experience in the fields of technology transfer, innovation management, project management and grant application. Link: http://www.fortschrittswerkhaus.example The color of the logo is not exactly advantageous and can be adjusted. There are currently no image worlds, these are to be selected by the designer. Abstract motifs are certainly an advantage here (10 motifs). It could also be made animated programming (network, etc. http://valmeta.brixlane.example/). In this case, a proposal has to be made, which we implement in terms of programming technology. The structure and contents of the existing pages are taken over and supplemented. Programming is done with TYPO3 in responsive form (bootstrap). Required are homepage, content page and contact page.

```html
<!DOCTYPE html>
<html lang="en">
<head>
<meta charset="utf-8">
<title>Fortschrittswerkhaus</title>
<link href="https://fonts.googleapis.com/css2?family=Exo+2:wght@500;600;700;800&family=Mulish:wght@400;600;700&display=swap" rel="stylesheet">
<style>
:root{
  --navy:#1b1ba0;
  --navy-deep:#0d0d7a;
  --red:#e3062c;
  --ink:#222;
  --muted:#666;
  --light:#f5f5f5;
  --white:#fff;
}
*{box-sizing:border-box;margin:0;padding:0}
html,body{width:1200px;height:3346px;overflow:hidden}
body{position:relative;font-family:"Mulish",sans-serif;color:var(--ink);background:var(--white)}
.abs{position:absolute}
.head{font-family:"Exo 2",sans-serif;font-weight:700;text-transform:uppercase}

/* header */
.site-header{left:0;top:0;width:1200px;height:107px;background:var(--white);z-index:5}
.brand{display:flex;align-items:center;gap:10px}
.brand-mark{width:14px;height:14px;background:var(--navy)}
.brand-name{color:var(--navy);font-family:"Exo 2",sans-serif;font-size:17px;font-weight:700}
.header-brand{left:167px;top:54px}
.main-nav{left:444px;top:56px;display:flex;gap:28px;font-family:"Exo 2",sans-serif;font-weight:600;font-size:15px;text-transform:uppercase;color:#222}

/* hero */
.hero{left:0;top:107px;width:1200px;height:660px}
.hero-photo{width:100%;height:100%;background:linear-gradient(100deg,#22264e 0%,#3a4474 45%,#8f96b0 75%,#5b6384 100%)}
.hero-title{left:152px;top:300px;color:var(--white);font-size:40px;line-height:42px;font-weight:700}
.hero-lead{left:158px;top:398px;color:var(--white);font-size:19px;line-height:31px}
.btn{display:inline-flex;align-items:center;justify-content:center;border-radius:30px;font-family:"Exo 2",sans-serif;font-weight:600;font-size:18px}
.btn-red{left:158px;top:489px;width:186px;height:54px;background:var(--red);color:var(--white)}

/* society */
.society-photo{left:0;top:714px;width:680px;height:580px;background:linear-gradient(90deg,#555 0%,#8a8a8a 45%,#cfcfcf 75%,#fff 100%)}
.society-title{left:618px;top:830px;font-size:34px;color:var(--navy)}
.rule{height:4px;width:62px;background:var(--navy)}
.society-rule{left:620px;top:878px}
.society-list{left:622px;top:902px;width:470px;font-size:16px;line-height:21px;color:#333;list-style:none}
.society-list li{margin-bottom:10px}
.btn-outline-red{left:620px;top:1144px;width:175px;height:52px;border:2px solid var(--red);color:var(--red);background:var(--white)}

/* services */
.services{left:0;top:1240px;width:1200px;height:690px;background:radial-gradient(ellipse at 75% 30%,#2a2ad0 0%,var(--navy) 40%,var(--navy-deep) 100%);clip-path:polygon(0 30px,100% 0,100% 100%,0 100%)}
.services-title{left:0;top:1355px;width:1200px;text-align:center;font-size:34px;color:var(--white)}
.services-rule{left:568px;top:1400px;background:var(--white)}
.service{width:220px;color:var(--white)}
.service-icon{width:70px;height:70px}
.service-name{margin-top:26px;font-size:16px;line-height:20px;font-weight:700}
.service-text{margin-top:10px;font-size:15px;line-height:22px;color:#aab0ff}
.service-link{margin-top:12px;font-size:12px;font-weight:800;font-family:"Exo 2",sans-serif}
.btn-outline-white{left:515px;top:1753px;width:172px;height:46px;border:2px solid var(--white);color:var(--white)}

/* reports */
.reports-title{left:0;top:1952px;width:1200px;text-align:center;font-size:31px;line-height:34px;color:var(--red)}
.reports-title span{color:var(--navy)}
.card{top:2070px;width:219px;height:294px;background:var(--white);border:2px solid #ddd}
.card-photo{height:161px;background:linear-gradient(160deg,#9aa 0%,#4a4e58 100%)}
.card-date{position:absolute;left:50%;top:149px;transform:translateX(-50%);background:var(--red);color:var(--white);font-size:13px;font-weight:700;padding:4px 20px}
.card-title{margin-top:28px;text-align:center;font-family:"Exo 2",sans-serif;font-weight:700;color:var(--navy);font-size:16px;line-height:19px;padding:0 10px}
.card-text{margin-top:8px;text-align:center;font-size:11px;line-height:15px;color:#777;padding:0 18px}
.arrow{width:30px;height:56px}

/* event */
.event-photo{left:0;top:2442px;width:1200px;height:520px;background:linear-gradient(90deg,#25245e 0%,#3a3a80 50%,#2a2a6e 100%)}
.event-title{left:0;top:2570px;width:1200px;text-align:center;font-size:30px;color:var(--white);font-weight:600}
.event-sub{left:0;top:2647px;width:1200px;text-align:center;font-size:19px;font-weight:700;color:var(--white)}
.event-text{left:250px;top:2686px;width:700px;text-align:center;font-size:18px;line-height:23px;color:var(--white)}
.btn-white{left:504px;top:2779px;width:184px;height:54px;background:var(--white);color:var(--navy);font-weight:700}

/* footer */
.site-footer{left:0;top:2925px;width:1200px;height:421px;background:var(--light);clip-path:polygon(0 30px,100% 0,100% 100%,0 100%)}
.footer-brand{left:167px;top:3056px}
.footer-brand .brand-name{font-size:15px}
.footer-col{top:3024px}
.footer-col h4{font-family:"Exo 2",sans-serif;font-weight:700;font-size:18px;color:var(--navy);text-transform:uppercase;margin-bottom:12px}
.footer-col ul{list-style:none;font-size:14px;line-height:27px;color:#666}
.social li{display:flex;align-items:center;gap:12px}
.social li::before{content:"";width:8px;height:8px;background:var(--navy)}
.footer-rule{left:0;top:3272px;width:1200px;height:1px;background:#ddd}
.copyright{left:0;top:3294px;width:1200px;text-align:center;font-size:14px;color:#444}
</style>
</head>
<body>

<header class="abs site-header">
  <div class="abs brand header-brand">
    <span class="brand-mark"></span>
    <span class="brand-name">FORTSCHRITTSWERKHAUS</span>
  </div>
  <nav class="abs main-nav">
    <span>Services</span><span>References</span><span>Events &amp; Workshops</span><span>Reports</span><span>Contact</span>
  </nav>
</header>

<section class="abs hero">
  <div class="hero-photo" role="img" aria-label="Business people in suits applauding at a conference"></div>
  <svg class="abs" style="left:0;bottom:0" width="1200" height="110" viewBox="0 0 1200 110">
    <polygon points="0,110 1200,30 1200,80 0,110" fill="#e3062c"/>
    <polygon points="500,110 1200,60 1200,90 900,110" fill="#1b1ba0"/>
    <polygon points="0,70 1200,90 1200,110 0,110" fill="#fff"/>
  </svg>
</section>
<h1 class="abs head hero-title">Welcome to<br>Fortschrittswerkhaus</h1>
<p class="abs hero-lead">Lorem ipsum dolor sit amet consectetuer adipiscing elit<br>Nam cursus Morbi ut mi Nullam enim leo egestas</p>
<a class="abs btn btn-red">Learn More</a>

<div class="abs society-photo" role="img" aria-label="Black and white photo of speakers standing at a table during an event"></div>
<h2 class="abs head society-title">The Innovation Society</h2>
<div class="abs rule society-rule"></div>
<ul class="abs society-list">
  <li>With whom can I implement my innovative idea?</li>
  <li>Who helps me develop new products, services or business models based on my abilities?</li>
  <li>How do I become more independent of my existing customers with my own products?</li>
  <li>Who protects my ideas?</li>
  <li>Who opens the doors to science for me if I do not know who the right people are?</li>
</ul>
<a class="abs btn btn-outline-red">Learn More</a>

<section class="abs services" role="img" aria-label="Deep blue background with abstract network pattern"></section>
<svg class="abs" style="left:0;top:1800px" width="1200" height="130" viewBox="0 0 1200 130">
  <polygon points="650,90 1200,40 1200,100" fill="#e3062c"/>
  <polygon points="0,130 0,118 1200,90 1200,130" fill="#fff"/>
</svg>
<h2 class="abs head services-title">Our Services</h2>
<div class="abs rule services-rule"></div>

<div class="abs service" style="left:163px;top:1456px">
  <svg class="service-icon" viewBox="0 0 70 70" fill="none" stroke="#fff" stroke-width="2"><path d="M8 24h50M48 14l10 10-10 10M62 46H12M22 36L12 46l10 10"/></svg>
  <div class="service-name head">Technology and<br>knowledge transfer</div>
  <div class="service-text">We support companies in implementing their innovative projects</div>
  <div class="service-link">READ MORE</div>
</div>
<div class="abs service" style="left:404px;top:1456px">
  <svg class="service-icon" viewBox="0 0 70 70" fill="none" stroke="#fff" stroke-width="2"><rect x="12" y="8" width="46" height="56" rx="3"/><path d="M20 24l4 4 8-8M20 40l4 4 8-8M38 24h12M38 40h12"/></svg>
  <div class="service-name head">Innovation and<br>project management</div>
  <div class="service-text">We support companies in implementing their innovative projects</div>
  <div class="service-link">READ MORE</div>
</div>
<div class="abs service" style="left:645px;top:1456px">
  <svg class="service-icon" viewBox="0 0 70 70" fill="none" stroke="#fff" stroke-width="2"><circle cx="35" cy="35" r="7"/><circle cx="12" cy="12" r="5"/><circle cx="58" cy="12" r="5"/><circle cx="12" cy="58" r="5"/><circle cx="58" cy="58" r="5"/><path d="M16 16l14 14M54 16L40 30M16 54l14-14M54 54L40 40"/></svg>
  <div class="service-name head">Cooperation and<br>network management</div>
  <div class="service-text">We support companies in implementing their innovative projects</div>
  <div class="service-link">READ MORE</div>
</div>
<div class="abs service" style="left:888px;top:1456px">
  <svg class="service-icon" viewBox="0 0 70 70" fill="none" stroke="#fff" stroke-width="2"><path d="M28 50c0-8-10-12-10-24a17 17 0 0134 0c0 12-10 16-10 24z"/><path d="M28 56h14M30 62h10"/></svg>
  <div class="service-name head">From ideas to<br>innovations</div>
  <div class="service-text">We support companies in implementing their innovative projects</div>
  <div class="service-link">READ MORE</div>
</div>
<a class="abs btn btn-outline-white">View More</a>

<h2 class="abs head reports-title">Reports on current<br><span>topics and events</span></h2>

<svg class="abs arrow" style="left:78px;top:2185px" viewBox="0 0 30 56"><path d="M26 2L4 28l22 26" fill="none" stroke="#666" stroke-width="3"/></svg>
<svg class="abs arrow" style="left:1080px;top:2185px" viewBox="0 0 30 56"><path d="M4 2l22 26L4 54" fill="none" stroke="#666" stroke-width="3"/></svg>

<article class="abs card" style="left:134px">
  <div class="card-photo" role="img" aria-label="Speaker presenting on stage"></div>
  <span class="card-date">09/10/2018</span>
  <h3 class="card-title">IoT - what<br>companies want</h3>
  <p class="card-text">Lorem ipsum dolor sit amet conse ctetuer adipiscing elit Nam</p>
</article>
<article class="abs card" style="left:368px">
  <div class="card-photo" role="img" aria-label="Visitors at an exhibition hall"></div>
  <span class="card-date">02/21/2018</span>
  <h3 class="card-title">In conversation with the Lindenfeld Velmarsee</h3>
  <p class="card-text">Lorem ipsum dolor sit amet conse ctetuer adipiscing elit Nam</p>
</article>
<article class="abs card" style="left:602px">
  <div class="card-photo" role="img" aria-label="Group photo of event participants"></div>
  <span class="card-date">02/14/2018</span>
  <h3 class="card-title">Engagement<br>Intensified</h3>
  <p class="card-text">Lorem ipsum dolor sit amet conse ctetuer adipiscing elit Nam</p>
</article>
<article class="abs card" style="left:834px">
  <div class="card-photo" role="img" aria-label="Speaker talking in a lecture room"></div>
  <span class="card-date">02/10/2017</span>
  <h3 class="card-title">Innovations in<br>mobile applications</h3>
  <p class="card-text">Lorem ipsum dolor sit amet conse ctetuer adipiscing elit Nam</p>
</article>

<div class="abs event-photo" role="img" aria-label="Conference attendees in conversation, tinted in deep blue"></div>
<svg class="abs" style="left:0;top:2440px" width="1200" height="80" viewBox="0 0 1200 80">
  <polygon points="0,0 0,70 1200,40 1200,0" fill="#fff"/>
  <polygon points="0,0 520,30 0,70" fill="#e3062c"/>
</svg>
<h2 class="abs head event-title">Event &amp; Workshop</h2>
<p class="abs event-sub">BrightStep conference on the 5th and 6th of September, 1818</p>
<p class="abs event-text">With the increasing use of digital technologies, the economy and society are changing. In order to remain internationally competitive, companies must increasingly offer "smart" products, ie intelligent products</p>
<a class="abs btn btn-white">View More</a>

<footer class="abs site-footer"></footer>
<div class="abs brand footer-brand">
  <span class="brand-mark"></span>
  <span class="brand-name">FORTSCHRITTSWERKHAUS</span>
</div>
<div class="abs footer-col" style="left:415px">
  <h4>Company</h4>
  <ul><li>Home</li><li>About Us</li><li>Why Us</li><li>Events &amp; Workshop</li></ul>
</div>
<div class="abs footer-col" style="left:578px">
  <h4>Services</h4>
  <ul><li>Innovation Idea</li><li>Project Management</li><li>Property Right</li><li>Network Management</li></ul>
</div>
<div class="abs footer-col" style="left:763px">
  <h4>Resources</h4>
  <ul><li>Blogs</li><li>Reports</li><li>Contact us</li></ul>
</div>
<div class="abs footer-col" style="left:921px">
  <h4>Get in touch</h4>
  <ul class="social"><li>Microposts</li><li>Community</li><li>Network</li><li>Gallery</li></ul>
</div>
<div class="abs footer-rule"></div>
<p class="abs copyright">Copyright © 2019 All right reserved</p>

</body>
</html>
```